Packaging Design for Boneless Picnic Ham

We are Bright Larder Limited, a company based in Trinidad which is located within the Caribbean. We produce and sell a plethora of meat products including a variety of hams, sausages and even bacon.

We require a packaging design for a ham product. This product is packaged within a cryovac (11" X 18") shrink bag which would be used to package our Boneless Picnic Ham which weighs 2.5 Kilograms.

The design space should be 7 inches wide and 6 inches in height. The design is 3 inches from the bottom and 2 inches off each side.

Our target audience comprises of caterers as well as the average household folk. What sets our product apart is that it is has a great taste, 20% less salt and is affordable and easy. We commonly refer to it as the "Oven Ready Roast".

Attached below, is our logo which you must incorporate onto the design. We also request that the header be "Applewood Cured Rolled Country Pork".

Target Market(s)

Caterers and Average Household Folk

Industry/Entity Type

It Company

Font styles to use
Sans Serif

Requirements
Must have
• The Bright Larder Company Logo and the header must have "Applewood Cured Rolled Country Pork"
Nice to have
• Maximum Creativity
Should not have
• No animal artwork should be included onto the design

```html
<!DOCTYPE html>
<html lang="en">
<head>
<meta charset="utf-8">
<title>Bright Larder – Boneless Picnic Ham Label</title>
<link rel="stylesheet" href="https://fonts.googleapis.com/css2?family=Oswald:wght@300;500;700&family=Tinos:wght@400;700&display=swap">
<style>
  :root {
    --stage: #f6f6f6;
    --gold: #e9c15a;
    --gold-deep: #c9962a;
    --orange: #e9a22e;
    --orange-light: #f2b845;
    --wave: #f6dc82;
    --red: #b3152b;
    --red-deep: #7c0b18;
    --navy: #1f2a78;
    --navy-deep: #131b55;
    --ink: #1b1b1b;
    --white: #ffffff;
  }
  html, body { margin: 0; padding: 0; overflow: hidden; background: var(--stage); }
  .canvas {
    position: relative; width: 1200px; height: 1200px; overflow: hidden;
    background: var(--stage); font-family: "Oswald", sans-serif;
  }
  .floor-shadow {
    position: absolute; left: 160px; top: 1070px; width: 880px; height: 40px;
    border-radius: 50%;
    background: radial-gradient(ellipse at center, rgba(0,0,0,0.22), rgba(0,0,0,0) 70%);
  }
  .label {
    position: absolute; left: 132px; top: 238px; width: 940px; height: 806px;
    box-sizing: border-box; border: 4px solid var(--gold);
    background: radial-gradient(circle at 62% 45%, var(--orange-light) 0%, var(--orange) 70%);
  }
  .label-frame {
    position: absolute; left: 10px; top: 10px; right: 10px; bottom: 10px;
    border: 2px solid var(--gold-deep);
  }
  .wave-ornament { position: absolute; left: 0; top: 0; }
  .brand-name {
    position: absolute; left: 316px; top: 222px; width: 600px; text-align: center;
    font-weight: 700; font-size: 70px; color: var(--navy); line-height: 1;
  }
  .product-header {
    position: absolute; left: 316px; top: 312px; width: 600px; text-align: center;
    font-weight: 500; font-size: 21px; letter-spacing: 2px; color: var(--navy);
    line-height: 1; margin: 0;
  }
  .product-photo {
    position: absolute; left: 262px; top: 370px; width: 690px; height: 480px;
    background:
      radial-gradient(ellipse 190px 150px at 520px 360px, #f3c4c0 0%, #eab0aa 55%, rgba(234,176,170,0) 80%),
      radial-gradient(ellipse 170px 170px at 380px 260px, #c65a48 0%, #b8452e 50%, rgba(184,69,46,0) 78%),
      radial-gradient(ellipse 200px 250px at 170px 240px, #bd4426 0%, #a8321c 55%, rgba(168,50,28,0) 80%);
  }
  .quality-badge {
    position: absolute; left: 223px; top: 368px; width: 140px; height: 140px;
    border-radius: 50%; box-sizing: border-box; border: 5px solid var(--gold);
    background: radial-gradient(circle at 40% 35%, #4a4a4a, var(--ink) 70%);
    display: flex; flex-direction: column; align-items: center; justify-content: center;
    font-family: "Tinos", serif; color: var(--gold); transform: rotate(-14deg);
    line-height: 1.05;
  }
  .quality-badge .word { font-size: 30px; }
  .quality-badge .rank { font-size: 30px; font-weight: 700; }
  .classic-ribbon { position: absolute; left: 956px; top: 238px; width: 58px; height: 370px; }
  .classic-text {
    position: absolute; left: 956px; top: 238px; width: 58px; height: 340px;
    display: flex; align-items: center; justify-content: center;
  }
  .classic-text span {
    transform: rotate(-90deg); font-family: "Tinos", serif; font-size: 44px;
    color: var(--gold); letter-spacing: 2px; white-space: nowrap;
  }
  .name-band {
    position: absolute; left: 132px; top: 818px; width: 940px; height: 184px;
    background: linear-gradient(90deg, var(--red-deep) 0%, var(--red) 30%, var(--red) 70%, var(--red-deep) 100%);
    border-top: 3px solid var(--gold); border-bottom: 3px solid var(--gold);
    box-sizing: border-box;
  }
  .product-name {
    position: absolute; left: 292px; top: 826px; width: 400px; color: var(--white);
    line-height: 1; margin: 0;
  }
  .product-name .cut { display: block; font-weight: 300; font-size: 92px; letter-spacing: 5px; }
  .product-name .kind { display: block; font-weight: 700; font-size: 88px; letter-spacing: -3px; margin-top: -8px; }
  .weight-box {
    position: absolute; left: 770px; top: 790px; width: 182px; height: 254px;
    box-sizing: border-box; border: 3px solid var(--gold); border-bottom: none;
    border-radius: 10px 10px 0 0;
    background: linear-gradient(180deg, var(--navy) 0%, var(--navy-deep) 100%);
    display: flex; flex-direction: column; align-items: center; justify-content: center;
    color: var(--white); line-height: 1;
  }
  .weight-box .lead { font-weight: 700; font-size: 50px; }
  .weight-box .amount { font-weight: 700; font-size: 118px; color: var(--gold); margin: -4px 0 -6px; }
  .weight-box .unit { font-weight: 500; font-size: 33px; }
</style>
</head>
<body>
<div class="canvas">
  <div class="floor-shadow"></div>

  <div class="label">
    <div class="label-frame"></div>
  </div>

  <svg class="wave-ornament" width="1200" height="1200" viewBox="0 0 1200 1200" role="img" aria-label="Soft yellow checked cloth banner behind the brand name">
    <path d="M230 258 C360 240 470 150 578 100 C700 170 820 150 920 270 C860 300 820 330 770 380 C700 420 640 400 570 440 C500 420 420 330 300 300 Z" fill="var(--wave)"/>
  </svg>

  <div class="brand-name">Bright Larder</div>
  <h2 class="product-header">APPLEWOOD CURED ROLLED COUNTRY PORK</h2>

  <div class="product-photo" role="img" aria-label="Glazed boneless ham, whole and sliced, with red berries and leaves"></div>

  <div class="quality-badge">
    <span class="word">Quality</span>
    <span class="rank">No.1</span>
  </div>

  <svg class="classic-ribbon" viewBox="0 0 58 370" width="58" height="370">
    <path d="M0 0 H58 V370 L29 345 L0 370 Z" fill="var(--red-deep)"/>
    <path d="M4 0 H54 V360 L29 338 L4 360 Z" fill="none" stroke="var(--gold)" stroke-width="2"/>
  </svg>
  <div class="classic-text"><span>CLASSIC</span></div>

  <div class="name-band"></div>
  <h1 class="product-name">
    <span class="cut">BONELESS</span>
    <span class="kind">PICNICHAM</span>
  </h1>

  <div class="weight-box">
    <span class="lead">WEIGHS</span>
    <span class="amount">2.5</span>
    <span class="unit">KILOGRAMS</span>
  </div>
</div>
</body>
</html>
```